interior designer/stylist looking for a letter press business card to reflect the stylish work

Hello Designers,
I need a business card design for an company called Halvard Interior Design. I'm aiming at the high end residential and private client market in London providing sleek simple interiors. I'd like my business card to be tackboard worthy and expensive looking, i want people to pin it and for it to have a sought after look, and want prospective customers to hire me as their interior designer as my card is so beautiful.
I love letter press design. I also like the use of colour/foil on the edge.
Colour combos & general things I like -
Black and White
Navy Blue and Gold
Neutral colours (muted palette of greys whites navys beiges)
White Marble & brass
Morvane (fashion designer)
....also open to other suggestions....
Please dont take the pink in the attached photos too literally. i'd like the card to look more masculine than feminine.
I'd like Halvard on one side in one font, with interior design underneath so one word will make the statement....... unless anyone has any other ideas, open to suggestions.
I'd like a really simple font and for the whole card to look very graphic.
my details -
Petra Quillby
Interior Designer & Stylist
email petra@halvardinteriordesign.co.uk
phone +447813554019
website wwww.halvardinteriordesign.co.uk
GO GO GO!! EXCITED TO SEE THE OUTCOME!!
x L
Target Market(s)
High End Residential and private clients
Industry/Entity Type
Business
Contact Information for Business Card
Halvard Interior Design & Styling
Petra Quillby
phone +447813554019

```html
<!DOCTYPE html>
<html lang="en">
<head>
<meta charset="utf-8">
<title>Halvard Interior Design — Business Card</title>
<link rel="stylesheet" href="https://fonts.googleapis.com/css2?family=Courier+Prime:wght@400;700&family=Open+Sans:wght@700&display=swap">
<style>
  :root {
    --backdrop: #b4b4b4;
    --card-white: #ffffff;
    --ink-teal: #2f7386;
    --card-teal: #1a576b;
    --press-teal: #5b8e9d;
  }
  html, body {
    margin: 0;
    padding: 0;
    overflow: hidden;
  }
  .canvas {
    position: relative;
    width: 1200px;
    height: 1000px;
    background: var(--backdrop);
    overflow: hidden;
  }
  .card {
    position: absolute;
    width: 735px;
    height: 419px;
    box-sizing: border-box;
    text-align: center;
  }
  .card--front {
    left: 30px;
    top: 82px;
    background: var(--card-white);
    color: var(--ink-teal);
    font-family: "Courier Prime", "Courier New", monospace;
  }
  .card--back {
    left: 425px;
    top: 534px;
    background: var(--card-teal);
    color: var(--press-teal);
    font-family: "Open Sans", Arial, sans-serif;
    font-weight: 700;
  }
  .holder {
    position: absolute;
    left: 0;
    right: 0;
    top: 152px;
  }
  .holder__name {
    margin: 0;
    font-size: 31px;
    font-weight: 400;
    letter-spacing: 1px;
    line-height: 38px;
  }
  .holder__role {
    margin: 0;
    font-size: 17px;
    font-weight: 700;
    letter-spacing: 1px;
    line-height: 22px;
  }
  .contact {
    position: absolute;
    left: 0;
    right: 0;
    top: 298px;
    margin: 0;
    font-size: 17px;
    font-weight: 700;
    letter-spacing: 0.6px;
    line-height: 23px;
    font-style: normal;
  }
  .contact span { display: block; }
  .brand {
    position: absolute;
    left: 0;
    right: 0;
    top: 128px;
  }
  .brand__name {
    margin: 0;
    font-size: 78px;
    line-height: 90px;
    letter-spacing: 1px;
  }
  .brand__tagline {
    margin: 0;
    font-size: 37px;
    line-height: 48px;
    letter-spacing: 0;
  }
</style>
</head>
<body>
<main class="canvas">
  <section class="card card--front" aria-label="Card front">
    <div class="holder">
      <h1 class="holder__name">Petra Quillby</h1>
      <p class="holder__role">Interior Designer and Stylist</p>
    </div>
    <address class="contact">
      <span class="contact__phone">+447813554019</span>
      <span class="contact__email">petra@halvardinteriordesign.co.uk</span>
      <span class="contact__web">www.halvardinteriordesign.co.uk</span>
    </address>
  </section>

  <section class="card card--back" aria-label="Card back">
    <div class="brand">
      <p class="brand__name">HALVARD</p>
      <p class="brand__tagline">INTERIOR DESIGN</p>
    </div>
  </section>
</main>
</body>
</html>
```